Express envelope design for courier company

We're a courier company launching a new service for sending documents around Australia. We need a design for the express envelope that will be used to hold the documents during transit. The envelope will be printed in colour on cardboard. Please see brief attached.

Design cues:
• Vibrant
• Simplified
• Clean
• Aesthetically pleasing
• Artistic
• Nothing “institutional” or “Harwick Lines”
• Nothing cramped, no small text

It's fine to crop, recolour, or reinterpret the logo.

Industry/Entity Type

It Company

Font styles to use
Sans Serif

Requirements
Must have
• Dimensions:
• Back side: 350 x 230 mm
• Front side: 387.5 x 230 mm (including flap to close envelope)
• Back side barcode panel: 90 x 75 mm (blank area for adhesive barcode)
• Back side address panel: 150 x 90 mm (see PDF for contents and layout)
• Front side text:
• QM-DR
• Express Envelope
• Sent With Care
• 1300 975 708
• qmdr.example
• Back side text:
• For documents
• Max. weight 500g, max width 20mm
• Sent With Care
• • Time-guaranteed and next-flight-out service for vital deliveries
• • Same-day and next-day local services
• • Overnight service to most Australian locations
• • Budget road service Australia-wide
• • Worldwide express courier
• Visit qmdr.example or phone 1300 975 708
• Flap text:
• Go to qmdr.example to book your pickup.
• Carried subject to QM-DR Standard Conditions of Carriage; see our website.
Nice to have
• Our web colours:
• #fcd614
• #d06517
• #3b5274
• #f0f0d8
• #382a3a

```html
<!DOCTYPE html>
<html lang="en">
<head>
<meta charset="utf-8">
<title>QM-DR Express Envelope</title>
<link href="https://fonts.googleapis.com/css2?family=Montserrat:ital,wght@0,300;0,400;0,500;0,600;0,700;1,600&display=swap" rel="stylesheet">
<style>
  :root {
    --yellow: #fcd614;
    --orange: #d06517;
    --navy: #3b5274;
    --cream: #f0f0d8;
    --plum: #382a3a;
    --flap: #e8e8cc;
    --rule: #e2e2c6;
    --stage: #ececec;
    --white: #ffffff;
  }
  * { box-sizing: border-box; margin: 0; padding: 0; }
  html, body { width: 1200px; height: 1200px; overflow: hidden; }
  body {
    background: var(--stage);
    font-family: "Montserrat", Arial, sans-serif;
    position: relative;
  }
  .envelope {
    position: absolute;
    left: 193px;
    width: 814px;
    height: 483px;
    background: var(--cream);
  }
  .envelope--back { top: 70px; }
  .envelope--front { top: 617px; }

  .flap {
    position: absolute;
    top: 0;
    width: 79px;
    height: 100%;
    background: var(--flap);
    display: flex;
    align-items: center;
    justify-content: center;
  }
  .envelope--back .flap { left: 0; border-right: 1px solid var(--rule); }
  .envelope--front .flap { right: 0; border-left: 1px solid var(--rule); }
  .flap__text {
    transform: rotate(-90deg);
    white-space: nowrap;
    font-size: 11.5px;
    line-height: 20px;
    color: var(--plum);
    text-align: center;
  }

  /* back side */
  .docs-heading {
    position: absolute; left: 110px; top: 38px;
    font-size: 34px; font-weight: 500; color: var(--navy);
  }
  .docs-limits {
    position: absolute; left: 112px; top: 80px;
    font-size: 12.5px; font-weight: 700; color: var(--navy);
  }
  .services {
    position: absolute; left: 112px; top: 104px;
    width: 450px;
    list-style: none;
    font-size: 13.5px; line-height: 22px; color: var(--navy);
  }
  .services li::before {
    content: ""; display: inline-block;
    width: 6px; height: 6px; border-radius: 50%;
    background: var(--navy); margin-right: 9px; vertical-align: 2px;
  }
  .tagline--back {
    position: absolute; left: 585px; top: 22px;
    font-size: 30px; font-weight: 300; line-height: 36px; color: var(--orange);
  }
  .address-frame { position: absolute; left: 0; top: 0; }
  .address-field {
    position: absolute;
    font-size: 12.5px; color: var(--plum);
    border-bottom: 1px solid var(--rule);
    padding: 8px 0 0 10px;
  }
  .address-field--sender { left: 124px; top: 234px; width: 447px; height: 32px; }
  .address-field--receiver { left: 124px; top: 266px; width: 447px; height: 100px; }
  .address-field--state { left: 124px; top: 366px; width: 220px; height: 50px; border-bottom: none; border-right: 1px solid var(--rule); padding-top: 28px; }
  .address-field--postcode { left: 344px; top: 366px; width: 227px; height: 50px; border-bottom: none; padding-top: 8px; }
  .contact-line {
    position: absolute; left: 122px; top: 440px;
    font-size: 14px; color: var(--navy);
  }
  .contact-line strong { font-weight: 700; }

  /* front side */
  .brand-block {
    position: absolute; left: 28px; top: 30px;
    width: 414px; height: 272px;
    background: var(--plum);
    border-top-left-radius: 18px;
  }
  .brand-name {
    position: absolute; left: 36px; top: 80px;
    font-size: 34px; font-weight: 600; color: var(--white);
  }
  .tagline-block {
    position: absolute; left: 452px; top: 30px;
    width: 272px; height: 272px;
    background: var(--yellow);
    border-top-right-radius: 18px;
    border-left: 3px solid #e6bf10;
  }
  .tagline--front {
    position: absolute; left: 16px; bottom: 10px;
    font-size: 30px; font-weight: 300; line-height: 36px; color: var(--white);
  }
  .product-name {
    position: absolute; left: 48px; top: 322px;
    font-size: 38px; font-weight: 600; font-style: italic;
    font-variant: small-caps; letter-spacing: 0.5px;
    color: var(--navy);
  }
  .accent-bar {
    position: absolute; left: 28px; top: 392px;
    width: 414px; height: 66px;
    background: var(--orange);
    border-bottom-left-radius: 18px;
    border-top: 3px solid #b9570f;
  }
  .contact-block {
    position: absolute; left: 452px; top: 392px;
    width: 272px; height: 66px;
    background: var(--navy);
    border-bottom-right-radius: 18px;
    padding: 6px 0 0 14px;
    font-size: 19px; line-height: 27px; font-weight: 400; color: var(--white);
  }
</style>
</head>
<body>

  <section class="envelope envelope--back" aria-label="Envelope back side">
    <div class="flap">
      <p class="flap__text">Go to qmdr.example to book your pickup.<br>Carried subject to QM-DR Standard Conditions of Carriage; see our website.</p>
    </div>

    <h2 class="docs-heading">For documents</h2>
    <p class="docs-limits">Max. weight 500g, max width 20mm</p>
    <ul class="services">
      <li>Time-guaranteed and next-flight-out service for vital deliveries</li>
      <li>Same-day and next-day local services</li>
      <li>Overnight service to most Australian locations</li>
      <li>Budget road service Australia-wide</li>
      <li>Worldwide express courier</li>
    </ul>
    <p class="tagline--back">Sent<br>With Care</p>

    <svg class="address-frame" width="814" height="483" viewBox="0 0 814 483">
      <path d="M140 230 H575 V130 Q575 110 595 110 H750 Q770 110 770 130 V350 Q770 370 750 370 H575 V400 Q575 420 555 420 H140 Q120 420 120 400 V250 Q120 230 140 230 Z"
            fill="#ffffff" stroke="#d06517" stroke-width="8" stroke-linejoin="round"/>
      <line x1="575" y1="226" x2="575" y2="374" stroke="#d06517" stroke-width="8"/>
    </svg>
    <div class="address-field address-field--sender">Sender's name</div>
    <div class="address-field address-field--receiver">Receiver</div>
    <div class="address-field address-field--state">State</div>
    <div class="address-field address-field--postcode">Postcode</div>

    <p class="contact-line">Visit <strong>qmdr.example</strong> or phone <strong>1300 975 708</strong></p>
  </section>

  <section class="envelope envelope--front" aria-label="Envelope front side">
    <div class="brand-block">
      <p class="brand-name">QM-DR</p>
    </div>
    <div class="tagline-block">
      <p class="tagline--front">Sent<br>With Care</p>
    </div>
    <h1 class="product-name">Express Envelope</h1>
    <div class="accent-bar"></div>
    <div class="contact-block">1300 975 708<br>qmdr.example</div>

    <div class="flap">
      <p class="flap__text">Go to qmdr.example to book your pickup.<br>Carried subject to QM-DR Standard Conditions of Carriage; see our website.</p>
    </div>
  </section>

</body>
</html>
```